Book Cover for Physics Book
BrightLabScience.net
Project: Book Cover for Physics Book
Book Cover for Physics Book - Education
Creative Brief
Education
High school students. Should be colorful, bright, shiny, engaging, made to stand out. Cover will also be used for Vendora e-book cover, so title should be large enough to be easily read when image size is reduced.
Templates for sizing attached. Title and author must appear on front cover as well as bound edge. Back cover leave bar code area blank (publisher will place bar code here). Quirky Otter Studios logo should appear somewhere on back cover. BrightLabScience.net logo may be used as part of the design of front or back cover, or may be skipped completely. Back cover text: Core Mechanics Primer is an easy-to-read guide to the entire Core Mechanics course, featuring more than 500 worked-out problems with full solutions and deeper understanding questions. Core Mechanics Primer covers all major topics included in the Core Mechanics course, including: kinematics, dynamics, momentum, impulse, gravity, uniform circular motion, rotation, work, energy, power, mechanical waves, sound, electrostatics, and circuits. This book is designed to assist physics students in their high school Core Mechanics courses both as a guide throughout the course as well as a review book to guide end-of-course exam preparation. Core Mechanics Primer is integrated with the BrightLabScience.net website, which includes online question and answer forums, videos, animations, and supplemental problems to help you master the essential concepts of physics.
Concepts
KMarwick KMarwick
Also, please don't think you have to use stock photos -- illustrations and creative ideas are very much appreciated as well!
Also, just to provide some ideas, the following PixelVault images would probably relate to the book fairly well: 259173804, 362810571 Other topics covered include things like amusement park rides (things that spin, roller coasters, etc.), all of which might make interesting front cover items. Lots of great designs so far, thanks for your hard work!
Topics covered in the book include: motion (kinematics) forces (dynamics) momentum, collisions, and explosions work, energy, power circular and rotational motion pendulums, springs, and swings waves and sound electricity and circuits
Looking forward to seeing what exciting and creative designs you can put forth for this new physics book! Target audience is high school students (15-17 years of age) taking physics. Sales into this target range many times are dependent on a catchy cover, so think bright, fun, and colorful for this age range.

```html
<!DOCTYPE html>
<html lang="en">
<head>
<meta charset="utf-8">
<title>Core Mechanics Primer – Book Cover</title>
<link rel="stylesheet" href="https://fonts.googleapis.com/css2?family=Oswald:wght@500;700&family=Open+Sans:wght@400;600&display=swap">
<style>
  :root {
    --backdrop: #e9e4dc;
    --navy: #243a6e;
    --navy-deep: #1c2f5c;
    --gold: #f7c21a;
    --white: #ffffff;
    --sky-1: #0e2a5a;
    --sky-2: #2f6fb4;
    --sky-3: #8fc6ee;
  }
  * { margin: 0; padding: 0; box-sizing: border-box; }
  html, body { width: 1200px; height: 691px; overflow: hidden; background: var(--backdrop); }
  .canvas { position: relative; width: 1200px; height: 691px; }

  .book {
    position: absolute; left: 139px; top: 48px; width: 936px; height: 595px;
    display: flex; box-shadow: 0 8px 24px rgba(0,0,0,.25);
  }

  .back-cover {
    width: 317px; height: 100%; background: var(--navy); position: relative;
    padding: 40px 24px 0;
  }
  .back-title {
    font-family: "Oswald", sans-serif; font-weight: 700; color: var(--gold);
    font-size: 36px; line-height: 1.12;
  }
  .back-copy {
    margin-top: 22px; font-family: "Open Sans", sans-serif; color: var(--white);
    font-size: 8.3px; line-height: 1.45;
  }
  .back-copy p + p { margin-top: 9px; }
  .publisher {
    position: absolute; left: 24px; bottom: 30px; display: flex; align-items: center; gap: 10px;
  }
  .publisher-mark { width: 30px; height: 30px; border-radius: 50%; background: var(--gold); }
  .publisher-name {
    font-family: "Open Sans", sans-serif; font-weight: 600; font-size: 11px; color: var(--gold);
  }

  .spine {
    width: 58px; height: 100%; background: var(--navy-deep);
    display: flex; flex-direction: column; align-items: center; justify-content: space-between;
    padding: 30px 0 28px;
  }
  .spine-title, .spine-author {
    writing-mode: vertical-rl; font-family: "Oswald", sans-serif; font-weight: 700;
    font-size: 26px; white-space: nowrap;
  }
  .spine-title { color: var(--white); }
  .spine-author { color: var(--gold); }

  .front-cover { width: 561px; height: 100%; display: flex; flex-direction: column; background: var(--white); }
  .front-head { position: relative; height: 216px; padding: 58px 0 0 62px; }
  .front-title {
    font-family: "Oswald", sans-serif; font-weight: 700; font-size: 58px; line-height: 1.08;
    color: var(--navy);
  }
  .front-title .accent { display: block; color: var(--gold); }
  .rocket-art {
    position: absolute; right: 40px; top: 14px; width: 40px; height: 70px;
  }
  .cover-art { height: 300px; }
  .front-foot {
    flex: 1; background: var(--navy); display: flex; align-items: center; justify-content: center;
  }
  .author-plate {
    background: var(--gold); color: var(--navy); font-family: "Oswald", sans-serif;
    font-weight: 700; font-size: 26px; padding: 4px 30px; border-radius: 3px;
  }
</style>
</head>
<body>
<main class="canvas">
  <div class="book">
    <section class="back-cover">
      <h2 class="back-title">Core Mechanics<br>Primer</h2>
      <div class="back-copy">
        <p>Core Mechanics Primer is an easy-to-read guide to the entire Core Mechanics course, featuring more than 500 worked-out problems with full solutions and deeper understanding questions. Core Mechanics Primer covers all major topics included in the Core Mechanics course, including: kinematics, dynamics, momentum, impulse, gravity, uniform circular motion, rotation, work, energy, power, mechanical waves, sound, electrostatics, and circuits.</p>
        <p>This book is designed to assist physics students in their high school Core Mechanics courses both as a guide throughout the course as well as a review book to guide end-of-course exam preparation.</p>
        <p>Core Mechanics Primer is integrated with the BrightLabScience.net website, which includes online question and answer forums, videos, animations, and supplemental problems to help you master the essential concepts of physics.</p>
      </div>
      <div class="publisher">
        <span class="publisher-mark"></span>
        <span class="publisher-name">Quirky Otter Studios</span>
      </div>
    </section>

    <section class="spine">
      <span class="spine-title">Core Mechanics Primer</span>
      <span class="spine-author">Kay Marwick</span>
    </section>

    <section class="front-cover">
      <header class="front-head">
        <h1 class="front-title">Core Mechanics<span class="accent">Primer</span></h1>
        <svg class="rocket-art" role="img" aria-label="Small illustration of a rocket launching" viewBox="0 0 40 70">
          <defs>
            <linearGradient id="rocketTone" x1="0" y1="0" x2="0" y2="1">
              <stop offset="0" stop-color="#9fb4d6"/>
              <stop offset="1" stop-color="#f7c21a"/>
            </linearGradient>
          </defs>
          <rect width="40" height="70" rx="6" fill="url(#rocketTone)" opacity=".55"/>
        </svg>
      </header>
      <svg class="cover-art" role="img" aria-label="Abstract blue background of glowing curved light trails and graph lines" viewBox="0 0 561 300" preserveAspectRatio="none">
        <defs>
          <linearGradient id="artTone" x1="0" y1="1" x2="1" y2="0">
            <stop offset="0" stop-color="var(--sky-1)"/>
            <stop offset=".6" stop-color="var(--sky-2)"/>
            <stop offset="1" stop-color="var(--sky-3)"/>
          </linearGradient>
        </defs>
        <rect width="561" height="300" fill="url(#artTone)"/>
      </svg>
      <footer class="front-foot">
        <span class="author-plate">Kay Marwick</span>
      </footer>
    </section>
  </div>
</main>
</body>
</html>
```